Software Engineering Company need eye catching banner for and Engineering conventions

We need an eye-catching banner designed. The size of the banner will be 34" W x 81" H. We develop routing software installed in bus systems and use GPS real-time tracking to always know where they are. We would like the banner to be dominated by the colors in our logo, 2 different blues, dark gray and of course white and black if needed. We are hoping for something that will pop out and look awesome. If you want to use our entire name or just our logo is completely up to you.

Target Market(s)

Young Engineers looking for new and cutting edge job opportunities

Industry/Entity Type

Computer Software

Colors
1f68ae
3779b6
ffffff

Requirements
Should not have
• the colors in our logo

```html
<!DOCTYPE html>
<html lang="en">
<head>
<meta charset="utf-8">
<title>Veyra Systems – Roll-up Banner</title>
<link href="https://fonts.googleapis.com/css2?family=Raleway:wght@400;500;600;700&display=swap" rel="stylesheet">
<style>
  :root {
    --blue-dark: #1f68ae;
    --blue-mid: #3779b6;
    --blue-light: #4fb0e6;
    --gray-dark: #555a60;
    --gray-text: #6a6e73;
    --white: #ffffff;
    --page-bg: #d3e0f0;
  }
  * { margin: 0; padding: 0; box-sizing: border-box; }
  html, body {
    width: 1200px; height: 2635px; overflow: hidden;
    background: var(--page-bg);
    font-family: "Raleway", sans-serif;
  }
  .banner {
    position: absolute; left: 60px; top: 32px;
    width: 1080px; height: 2570px;
    box-shadow: 0 10px 30px rgba(0,0,0,.18);
    background: var(--white);
  }
  .banner svg { display: block; width: 100%; height: 100%; }
  .brand-name { font-weight: 700; fill: var(--blue-dark); font-size: 28px; letter-spacing: 0.5px; }
  .title { font-weight: 600; font-size: 47px; }
  .title-accent { fill: var(--blue-dark); }
  .title-main { fill: var(--gray-dark); }
  .eyebrow { font-weight: 500; font-size: 16.5px; fill: var(--gray-dark); }
  .headline { font-weight: 500; font-size: 29px; fill: var(--blue-dark); }
  .intro { font-weight: 400; font-size: 14.2px; fill: var(--gray-text); }
  .feature-title { font-weight: 500; font-size: 13.5px; fill: var(--blue-dark); }
  .feature-body { font-weight: 400; font-size: 11.3px; fill: var(--gray-text); }
  .contact { font-weight: 500; font-size: 14px; fill: var(--white); }
</style>
</head>
<body>
<div class="banner">
  <svg viewBox="0 0 600 1428" xmlns="http://www.w3.org/2000/svg">
    <defs>
      <linearGradient id="heroTone" x1="0" y1="0" x2="0" y2="1">
        <stop offset="0" stop-color="#6b95d6"/>
        <stop offset="0.28" stop-color="#a9c5e7"/>
        <stop offset="0.36" stop-color="#caa947"/>
        <stop offset="0.65" stop-color="#e3b325"/>
        <stop offset="1" stop-color="#6a6040"/>
      </linearGradient>
    </defs>

    <!-- hero image area -->
    <rect class="hero-image" role="img" aria-label="Photo of yellow school buses under a blue sky, with a winding road illustration and map pin across its lower edge" x="0" y="0" width="600" height="840" fill="url(#heroTone)"/>

    <!-- brand -->
    <g class="brand">
      <rect x="164" y="82" width="42" height="42" fill="var(--blue-dark)"/>
      <text class="brand-name" x="218" y="114">VEYRA SYSTEMS</text>
    </g>

    <!-- title panel -->
    <polygon class="title-panel" points="0,256 418,256 380,480 0,480" fill="#ffffff"/>
    <text class="title" x="38">
      <tspan class="title-accent" x="38" y="329">Innovative</tspan>
      <tspan class="title-main" x="38" y="386">Transportation</tspan>
      <tspan class="title-main" x="38" y="443">Solutions</tspan>
    </text>

    <!-- intro -->
    <text class="eyebrow" x="22" y="878">Goal oriented</text>
    <text class="headline">
      <tspan x="22" y="910">Write your headline here lorem ipsum</tspan>
      <tspan x="22" y="943">dolor sit amet</tspan>
    </text>
    <text class="intro">
      <tspan x="22" y="973">Lorem ipsum dolor sit amet, consectetuer adipiscing elit, sed diam nonummy nibh</tspan>
      <tspan x="22" y="992.5">euismod tincidunt ut laoreet dolore magna aliquam erat volutpat. Ut wisi enim ad</tspan>
      <tspan x="22" y="1012">minim veniam, quis nostrud exerci tation ullamcorper suscipit lobortis nisl ut aliquip</tspan>
      <tspan x="22" y="1031.5">ex ea commodo consequat.</tspan>
    </text>

    <!-- features -->
    <g class="feature feature-technology">
      <g fill="none" stroke="var(--gray-dark)" stroke-width="2">
        <path d="M100,1102 L110,1102 L110,1118"/>
        <path d="M118,1082 L118,1118"/>
        <path d="M126,1094 L126,1118"/>
        <path d="M126,1094 L140,1094"/>
        <path d="M126,1104 L140,1104"/>
      </g>
      <circle cx="100" cy="1102" r="4.5" fill="var(--blue-mid)"/>
      <circle cx="112" cy="1086" r="4" fill="var(--blue-mid)"/>
      <circle cx="142" cy="1094" r="4" fill="var(--blue-mid)"/>
      <circle cx="142" cy="1104" r="4" fill="var(--blue-mid)"/>
      <text class="feature-title" x="172" y="1074">Technology</text>
      <text class="feature-body">
        <tspan x="172" y="1090">Lorem ipsum dolor sit amet, consectetuer adipiscing elit, sed diam</tspan>
        <tspan x="172" y="1105">nonummy nibh euismod tincidunt ut laoreet dolore magna.Lorem</tspan>
        <tspan x="172" y="1120">ipsum dolor sit amet, consectetuer adipiscing elit, sed diam</tspan>
      </text>
    </g>

    <g class="feature feature-cloud">
      <path fill="var(--blue-mid)" d="M92,1194 A12,12 0 0 1 96,1171 A16,16 0 0 1 126,1168 A13,13 0 0 1 142,1182 A12,12 0 0 1 136,1194 Z"/>
      <text class="feature-title" x="164" y="1149">Cloud</text>
      <text class="feature-body">
        <tspan x="164" y="1165">Lorem ipsum dolor sit amet, consectetuer adipiscing elit, sed diam</tspan>
        <tspan x="164" y="1180">nonummy nibh euismod tincidunt ut laoreet dolore magna.Lorem</tspan>
        <tspan x="164" y="1195">ipsum dolor sit amet, consectetuer adipiscing elit, sed diam</tspan>
      </text>
    </g>

    <g class="feature feature-gps">
      <polygon points="96,1244 111,1238 111,1276 96,1282" fill="#3aa85a"/>
      <polygon points="111,1238 127,1244 127,1282 111,1276" fill="var(--blue-mid)"/>
      <polygon points="127,1244 142,1238 142,1276 127,1282" fill="var(--blue-dark)"/>
      <text class="feature-title" x="170" y="1224">GPS</text>
      <text class="feature-body">
        <tspan x="170" y="1240">Lorem ipsum dolor sit amet, consectetuer adipiscing elit, sed diam</tspan>
        <tspan x="170" y="1255">nonummy nibh euismod tincidunt ut laoreet dolore magna.Lorem</tspan>
        <tspan x="170" y="1270">ipsum dolor sit amet, consectetuer adipiscing elit, sed diam</tspan>
      </text>
    </g>

    <g class="feature feature-secure">
      <path fill="var(--blue-dark)" d="M119,1306 L143,1315 L143,1333 C143,1346 133,1355 119,1362 C105,1355 95,1346 95,1333 L95,1315 Z"/>
      <circle cx="119" cy="1331" r="11" fill="#ffffff"/>
      <path d="M113,1331 L117.5,1335.5 L125,1327" fill="none" stroke="var(--blue-dark)" stroke-width="2.5"/>
      <text class="feature-title" x="170" y="1299">Secure</text>
      <text class="feature-body">
        <tspan x="170" y="1315">Lorem ipsum dolor sit amet, consectetuer adipiscing elit, sed diam</tspan>
        <tspan x="170" y="1330">nonummy nibh euismod tincidunt ut laoreet dolore magna.Lorem</tspan>
        <tspan x="170" y="1345">ipsum dolor sit amet, consectetuer adipiscing elit, sed diam</tspan>
      </text>
    </g>

    <!-- footer -->
    <polygon class="footer-accent" points="8,1367 600,1378 600,1390 8,1378" fill="var(--blue-light)"/>
    <polygon class="footer-band" points="12,1374 600,1386 600,1428 0,1428 0,1410" fill="var(--blue-dark)"/>
    <g class="contact-email">
      <rect x="120" y="1402" width="17" height="12" fill="#ffffff"/>
      <path d="M120,1402 L128.5,1409 L137,1402" fill="none" stroke="var(--blue-dark)" stroke-width="1.5"/>
      <text class="contact" x="149" y="1413">hr@veyrasystems.com</text>
    </g>
    <rect x="351" y="1396" width="1.5" height="24" fill="#ffffff"/>
    <g class="contact-phone">
      <path fill="#ffffff" d="M375,1400 L379,1399 L382,1405 L379.5,1407 C381,1410 383,1412 386,1413.5 L388,1411 L394,1414 L393,1418 C384,1418 375,1409 375,1400 Z"/>
      <text class="contact" x="400" y="1413">555.014.2280</text>
    </g>
  </svg>
</div>
</body>
</html>
```